A private security company called "Ventrell Security Services Ltd"

Hello everybody,

We need a web page for a company based in NZ. It is mainly an informative website so it would be wonderful if the designer puts their absolute best into making it a website that I would really appreciate. The website needs to show professionalism and also needs to make our web surfers find the information they need in a click. the company's colour is black and silver, and if those two colours could be integrated into the website it would be absolutely lovely. Please do contact me for any information.

Sincerely,
Dorian Valcourt

```html
<!DOCTYPE html>
<html lang="en">
<head>
<meta charset="utf-8">
<title>Ventrell Security Services Ltd</title>
<link rel="stylesheet" href="https://fonts.googleapis.com/css2?family=Montserrat:wght@300;400;600&family=Open+Sans:wght@400;600&display=swap">
<style>
:root{
  --navy:#050a1c;
  --navy-2:#0d1730;
  --ink:#111111;
  --text-grey:#555555;
  --page:#f3f3f3;
  --panel:#f7f6f6;
  --rule:#dcdcdc;
  --white:#ffffff;
  --silver:#b9bcc2;
  --footer:#0b0b0b;
}
*{box-sizing:border-box;margin:0;padding:0}
html,body{width:1024px;height:1200px;overflow:hidden}
body{position:relative;background:var(--page);font-family:"Montserrat",sans-serif;color:var(--ink)}
.site-header{position:absolute;left:0;top:0;width:1024px;height:139px;background:var(--white)}
.brand{position:absolute;left:96px;top:60px;display:flex;align-items:center;gap:12px}
.brand-dot{width:26px;height:26px;border-radius:50%;background:var(--ink)}
.brand-name{font-size:15px;font-weight:600;line-height:19px;color:var(--ink);text-transform:uppercase;letter-spacing:1px}
.call{position:absolute;right:94px;top:22px;font-size:19px;font-weight:300}
.call strong{font-weight:600}
.main-nav{position:absolute;right:88px;top:54px;display:flex;align-items:center;font-size:12.5px}
.main-nav a{color:var(--ink);text-decoration:none;padding:0 10px;line-height:30px}
.main-nav a.active{background:var(--navy);color:var(--white);font-weight:600;padding:0 11px;margin-right:0}
.hero{position:absolute;left:0;top:139px;width:1024px;height:385px;background:radial-gradient(ellipse at 62% 85%,#2a3448 0%,#0e1628 35%,var(--navy) 70%)}
.hero-title{position:absolute;left:94px;top:80px;color:var(--white);font-size:30px;line-height:34px}
.hero-title b{font-weight:600;display:block}
.hero-title span{font-weight:300;display:block}
.hero-copy{position:absolute;left:94px;top:175px;width:318px;color:var(--white);font-size:12.5px;line-height:16px}
.hero-btn{position:absolute;left:94px;top:280px;width:110px;height:42px;border:2px solid var(--white);color:var(--white);font-size:12.5px;display:flex;align-items:center;justify-content:center}
.hero-photo{position:absolute;left:627px;top:102px;width:298px;height:422px;border-radius:110px 110px 0 0;background:linear-gradient(180deg,#7a5a44 0%,#27314d 30%,#141b33 100%)}
.services{position:absolute;left:58px;top:563px;width:889px;height:382px;background:var(--panel)}
.service{position:absolute;top:22px;width:270px;text-align:center}
.service-icon{display:block;margin:0 auto}
.service-title{font-family:"Open Sans",sans-serif;font-size:14px;font-weight:400;margin-top:22px;height:20px}
.service-copy{font-family:"Open Sans",sans-serif;font-size:10.7px;line-height:17px;color:var(--text-grey);margin:20px auto 0;width:250px}
.service-btn{display:flex;align-items:center;justify-content:center;margin:29px auto 0;width:136px;height:36px;border:2px solid var(--navy);font-family:"Open Sans",sans-serif;font-weight:600;font-size:14px;color:var(--navy)}
.service-rule{position:absolute;top:366px;width:256px;height:3px;background:var(--rule)}
.gallery{position:absolute;top:968px;left:98px;display:flex;gap:21px}
.gallery-item{width:191px;height:143px;background:linear-gradient(135deg,#3a3a3a,#1d1d1d)}
.gallery-item.first{background:linear-gradient(135deg,#a5a8ab,#e6e6e6 55%,#3d3d3d)}
.site-footer{position:absolute;left:0;top:1156px;width:1024px;height:44px;background:var(--footer);color:var(--white);font-size:11.5px;display:flex;align-items:center;justify-content:center}
</style>
</head>
<body>
<header class="site-header">
  <div class="brand"><span class="brand-dot"></span><span class="brand-name">Ventrell<br>Security Services Ltd</span></div>
  <div class="call">Call: <strong>204 3187 552</strong></div>
  <nav class="main-nav">
    <a class="active" href="#">HOME</a><a href="#">About Us</a><a href="#">Security System</a><a href="#">Specialized Security</a><a href="#">Carreers</a><a href="#">Contact Us</a>
  </nav>
</header>

<section class="hero">
  <h1 class="hero-title"><b>Newzealand’s Best</b><span>Security Company</span></h1>
  <p class="hero-copy">It is a long established fact that a reader will be distracted by the readable content of a page when looking at its layout. The point of using Lorem Ipsum is that it has a more-or-less normal distribution of letters</p>
  <a class="hero-btn">READ MORE</a>
</section>
<div class="hero-photo" role="img" aria-label="Uniformed security officer standing with arms crossed"></div>

<section class="services">
  <div class="service" style="left:36px">
    <svg class="service-icon" width="92" height="98" viewBox="0 0 92 98"><circle cx="46" cy="46" r="44" fill="none" stroke="#050a1c" stroke-width="3"/><circle cx="46" cy="46" r="39" fill="#050a1c"/><path d="M40 89 46 97 52 89Z" fill="#050a1c"/><path d="M30 30 62 62M62 30 30 62" stroke="#fff" stroke-width="4"/><path d="M36 36h20v10c0 8-10 14-10 14s-10-6-10-14Z" fill="#050a1c" stroke="#fff" stroke-width="3"/></svg>
    <h2 class="service-title">SECURITY GUARDS</h2>
    <p class="service-copy">It is a long established fact that a reader will be distracted by the readable content of a page when looking at its layout. The point of using Lorem Ipsum is that it has a more-or-less normal distribution of letters, as opposed to using</p>
    <a class="service-btn">READ MORE</a>
  </div>
  <div class="service" style="left:317px">
    <svg class="service-icon" width="92" height="98" viewBox="0 0 92 98"><circle cx="46" cy="46" r="44" fill="none" stroke="#050a1c" stroke-width="3"/><circle cx="46" cy="46" r="39" fill="#050a1c"/><path d="M40 89 46 97 52 89Z" fill="#050a1c"/><path d="M46 24 66 31v13c0 12-9 20-20 24-11-4-20-12-20-24V31Z" fill="none" stroke="#fff" stroke-width="3"/><path d="M35 44l9 9 15-17" fill="none" stroke="#fff" stroke-width="4"/></svg>
    <h2 class="service-title">SPECIALIZED SECURITY</h2>
    <p class="service-copy">It is a long established fact that a reader will be distracted by the readable content of a page when looking at its layout. The point of using Lorem Ipsum is that it has a more-or-less normal distribution of letters, as opposed to using</p>
    <a class="service-btn">READ MORE</a>
  </div>
  <div class="service" style="left:599px">
    <svg class="service-icon" width="92" height="98" viewBox="0 0 92 98"><circle cx="46" cy="46" r="44" fill="none" stroke="#050a1c" stroke-width="3"/><circle cx="46" cy="46" r="39" fill="#050a1c"/><path d="M40 89 46 97 52 89Z" fill="#050a1c"/><rect x="24" y="30" width="44" height="14" fill="#fff"/><rect x="42" y="44" width="8" height="8" fill="#fff"/><path d="M46 52v12H34" fill="none" stroke="#fff" stroke-width="4"/><circle cx="46" cy="62" r="4" fill="#fff"/></svg>
    <h2 class="service-title">COMMERCIAL SECURITY SYSTEMS</h2>
    <p class="service-copy">It is a long established fact that a reader will be distracted by the readable content of a page when looking at its layout. The point of using Lorem Ipsum is that it has a more-or-less normal distribution of letters, as opposed to using</p>
    <a class="service-btn">READ MORE</a>
  </div>
  <div class="service-rule" style="left:44px"></div>
  <div class="service-rule" style="left:326px"></div>
  <div class="service-rule" style="left:607px"></div>
</section>

<div class="gallery">
  <div class="gallery-item first" role="img" aria-label="Security guard beside a patrol car"></div>
  <div class="gallery-item" role="img" aria-label="Surveillance camera on a wall"></div>
  <div class="gallery-item" role="img" aria-label="Security monitoring control room"></div>
  <div class="gallery-item" role="img" aria-label="Officer in white uniform shirt"></div>
</div>

<footer class="site-footer">Copyright © 2012-2014 Ventrell Security</footer>
</body>
</html>
```